Business Cards Brightvow Weddings

I have a new webpage address and would like to update my business cards with Facebook and Instagram links as well. I need assistance with designing it. I have attached an old business card.

Target Market(s)

Potential couples wanting to get married and vendors who work with weddings

Industry/Entity Type

Wedding

Contact Information for Business Card

Name of Company (Brightvow Weddings), Kay Whitfield, Phone number (480-555-0173), Webpage: www.brightvowweddings2go.example, Facebook Link: Brightvow Weddings, Instagram Link: BrightvowWeddings2go

Colors
0094D4
00A9DD
6FCCEA
C7EBF8
E9F6FB
00AB8E
00BBA5
67D7C9
C6EFE9
E9F9F6

Requirements
Nice to have
• Florals with teal on back of card. Not sure what needs to be on front and what on back
Should not have
• Definitive man/woman couple

```html
<!DOCTYPE html>
<html lang="en">
<head>
<meta charset="utf-8">
<title>Brightvow Weddings – Business Card</title>
<link rel="stylesheet" href="https://fonts.googleapis.com/css2?family=Playfair+Display:wght@400;700;900&display=swap">
<style>
  :root {
    --backdrop: #d8d8d8;
    --card-white: #ffffff;
    --brand-teal: #0a9aa3;
    --teal-deep: #079ca6;
    --teal-soft: #17a8ae;
    --teal-wordmark: #5cc3c0;
    --ink: #111111;
    --sketch-light: #f1f1f1;
    --sketch-mid: #dcdcdc;
  }
  * { margin: 0; padding: 0; box-sizing: border-box; }
  html, body {
    width: 1200px; height: 848px; overflow: hidden;
    background: var(--backdrop);
    font-family: "Playfair Display", Georgia, serif;
  }
  .sheet {
    position: relative; width: 1200px; height: 848px;
    display: flex; align-items: center; justify-content: center; gap: 50px;
  }
  .card {
    position: relative; width: 520px; height: 297px; overflow: hidden;
    box-shadow: 0 6px 18px rgba(0,0,0,0.12);
  }

  /* Front */
  .card-front { background: var(--card-white); }
  .floral-illustration {
    position: absolute; right: 0; top: 0; width: 230px; height: 235px;
    background: radial-gradient(ellipse at 60% 40%, var(--sketch-mid), var(--sketch-light) 70%, var(--card-white));
  }
  .wordmark-front {
    position: absolute; left: 38px; top: 92px;
    font-weight: 900; font-size: 38px; line-height: 0.95;
    color: var(--brand-teal); letter-spacing: -0.5px;
  }
  .wordmark-front .line-two { display: block; padding-left: 34px; }
  .person-name {
    position: absolute; left: 70px; top: 178px;
    font-weight: 900; font-size: 17px; color: var(--ink);
  }
  .contact-list {
    position: absolute; left: 46px; top: 202px; list-style: none;
  }
  .contact-item {
    display: flex; align-items: center; gap: 8px;
    font-size: 15px; color: var(--ink); height: 22px;
  }
  .contact-icon { width: 17px; height: 17px; flex: none; }

  /* Back */
  .card-back { background: var(--teal-deep); }
  .floral-pattern {
    position: absolute; inset: 0;
    background: linear-gradient(135deg, var(--teal-soft), var(--teal-deep) 50%, var(--teal-soft));
  }
  .wordmark-back {
    position: absolute; inset: 0;
    display: flex; flex-direction: column; align-items: center; justify-content: center;
    font-weight: 900; font-size: 62px; line-height: 0.95;
    color: var(--teal-wordmark); letter-spacing: -1px;
  }
  .wordmark-back .line-two { padding-left: 60px; }
</style>
</head>
<body>
<main class="sheet">
  <section class="card card-front" aria-label="Business card front">
    <div class="floral-illustration" role="img" aria-label="Line drawing of daffodils in black ink"></div>
    <h1 class="wordmark-front">Brightvow<span class="line-two">Weddings</span></h1>
    <p class="person-name">Kay Whitfield</p>
    <ul class="contact-list">
      <li class="contact-item">
        <svg class="contact-icon" viewBox="0 0 20 20" aria-hidden="true">
          <circle cx="10" cy="10" r="9" fill="none" stroke="var(--brand-teal)" stroke-width="1"/>
          <path d="M7 5.5l1.6 2.2-1 1.2c.6 1.3 1.4 2.1 2.6 2.6l1.2-1 2.2 1.6-.9 1.6c-3.6-.3-6.2-2.9-6.5-6.5z" fill="var(--brand-teal)"/>
        </svg>
        <span>480-555-0173</span>
      </li>
      <li class="contact-item">
        <svg class="contact-icon" viewBox="0 0 20 20" aria-hidden="true"><circle cx="10" cy="10" r="9" fill="none" stroke="var(--brand-teal)" stroke-width="1"/></svg>
        <span>BrightvowWeddings</span>
      </li>
      <li class="contact-item">
        <svg class="contact-icon" viewBox="0 0 20 20" aria-hidden="true"><circle cx="10" cy="10" r="9" fill="none" stroke="var(--brand-teal)" stroke-width="1"/></svg>
        <span>BrightvowWeddings2go</span>
      </li>
      <li class="contact-item">
        <svg class="contact-icon" viewBox="0 0 20 20" aria-hidden="true"><circle cx="10" cy="10" r="9" fill="none" stroke="var(--brand-teal)" stroke-width="1"/></svg>
        <span>www.brightvowweddings2go.example</span>
      </li>
    </ul>
  </section>

  <section class="card card-back" aria-label="Business card back">
    <div class="floral-pattern" role="img" aria-label="Faint repeating teal floral pattern"></div>
    <p class="wordmark-back"><span>Brightvow</span><span class="line-two">Weddings</span></p>
  </section>
</main>
</body>
</html>
```